Zielgruppe
Wohnungsbaugenossenschaft, Vermietung von Wohnungen
Mieter
Aufgabenstellung
Logo , siehe upload
- Standorte mit freien Wohnungen sollen dominant platziert werden
- aktuelle Meldungen, Havarienummer ( siehe hier: https://www.wbg-kelmsried.example/)
- weitere Kommunikationsdaten gut sichtbar, auch Öffnungszeiten

```html
<!DOCTYPE html>
<html lang="de">
<head>
<meta charset="utf-8">
<title>Wohnungsbaugenossenschaft Kelmsried eG</title>
<link rel="stylesheet" href="https://fonts.googleapis.com/css2?family=Comfortaa:wght@600;700&family=Open+Sans:ital,wght@0,300;0,400;0,600;0,700;1,300&family=Roboto+Condensed:wght@400;700&display=swap">
<style>
:root{
  --blue:#2f3e9c;
  --blue-dark:#46518f;
  --box1:#4b5592;
  --box2:#6a72b2;
  --box3:#8a91c8;
  --box4:#b1b6df;
  --lav:#a5aad8;
  --red:#e2001a;
  --grey:#f1f1f3;
  --text:#555a66;
  --white:#fff;
}
*{margin:0;padding:0;box-sizing:border-box}
html,body{width:1200px;height:2510px;overflow:hidden}
body{position:relative;font-family:"Open Sans",sans-serif;color:var(--text);background:var(--white);font-size:12px}
.abs{position:absolute}
.deco{font-family:"Comfortaa",sans-serif;font-weight:700;color:var(--blue)}
.cond{font-family:"Roboto Condensed",sans-serif}
.kicker{font-style:italic;font-weight:300;font-size:17px;color:#555}
.btn{display:inline-block;background:var(--red);color:#fff;font-family:"Roboto Condensed",sans-serif;font-size:12px;padding:4px 11px;text-transform:uppercase}
.icon{width:13px;height:13px;vertical-align:-2px;margin-right:6px;fill:currentColor}
/* top bar */
.topbar{top:0;left:0;width:1200px;height:38px}
.tagline{left:36px;top:11px;color:var(--red);font-style:italic;font-size:13px}
.havarie-top{left:434px;top:11px;font-size:12px;color:#666}
.meta-nav{right:34px;top:12px;font-size:10px;color:#999}
.meta-nav span{margin:0 5px}
/* nav */
.mainnav{top:38px;left:0;width:1200px;height:42px;background:var(--blue)}
.brand-box{left:35px;top:38px;width:122px;height:102px;background:#fff;z-index:3;display:flex;align-items:center;justify-content:center;flex-direction:column;gap:6px}
.brand-box .sq{width:22px;height:22px;background:var(--blue)}
.brand-box b{font-family:"Comfortaa",sans-serif;color:var(--blue);font-size:13px}
.site-title{left:167px;top:50px;color:#fff;font-size:17px;letter-spacing:.5px}
.nav-items{right:30px;top:54px;color:#fff;font-size:12px}
.nav-items span{margin:0 8px}
.nav-items .active{font-weight:700;position:relative}
.nav-items .active::before{content:"";position:absolute;left:-3px;right:-3px;top:-16px;height:4px;background:var(--red)}
/* hero */
.hero{top:80px;left:0;width:1200px;height:363px;background:linear-gradient(90deg,#b79f8c 0%,#e8d9c9 30%,#f5efe9 55%,#d8c7b6 80%,#a08570 100%)}
.hero h1{left:603px;top:136px;font-size:31px;line-height:39px;font-weight:600;text-transform:uppercase}
.hero-copy{left:605px;top:218px;font-size:13px;line-height:21px;color:#444;text-transform:uppercase}
.hero-btn{left:606px;top:286px}
/* info boxes */
.infobox{top:375px;width:284px;height:161px;color:#fff;padding:18px 0 0 30px}
.infobox h3{font-family:"Comfortaa",sans-serif;font-size:21px;font-weight:600;text-transform:uppercase;margin-bottom:10px}
.infobox h3 svg{width:21px;height:21px;fill:#fff;vertical-align:-3px;margin-right:6px}
.infobox p{font-size:11px;line-height:22px}
.hours p{line-height:18px}
.flat-card{left:621px;top:428px;width:240px;height:87px;background:#4d4f5c}
.flat-photo{left:0;top:0;width:120px;height:87px;background:linear-gradient(#8fb3dc,#d9c6a0 60%,#6d8a4a)}
.flat-card .txt{left:128px;top:6px;font-size:10px;line-height:12px;color:#fff}
.flat-card .dots{right:6px;bottom:4px;font-size:11px;letter-spacing:1px}
.service p{font-size:11px;line-height:13px;padding-right:24px}
.service .phone{font-size:20px;font-weight:700;margin-top:6px;color:#fff}
/* welcome */
.welcome-img{left:140px;top:555px;width:322px;height:275px;background:radial-gradient(ellipse at 50% 60%,#d9b39a,#51576e 70%,#fff 72%)}
.welcome-kicker{left:505px;top:562px}
.welcome h2{left:504px;top:580px;font-size:29px}
.welcome-text{left:505px;top:627px;width:620px;font-size:12.5px;line-height:16.5px;font-weight:300;color:#444}
.signoff{left:505px;top:727px;font-size:12.5px;font-weight:300;color:#444}
.signature{left:500px;top:752px;width:270px;height:58px;background:linear-gradient(90deg,rgba(80,80,90,.12),rgba(80,80,90,.04))}
/* market */
.market{top:830px;left:0;width:1200px;height:476px;background:var(--grey)}
.center{width:1200px;text-align:center;left:0}
.market-list{left:35px;top:975px;width:357px;height:268px;background:var(--lav)}
.market-list li{list-style:none;color:#fff;font-size:17.5px;height:41px;line-height:41px;padding-left:22px}
.market-list li.active{background:var(--red);height:48px;line-height:42px;margin-bottom:5px}
.market-head{left:426px;top:972px;width:742px;font-size:23px;border-bottom:1px solid var(--blue);padding-bottom:6px}
.card{top:1030px;width:234px;height:240px;background:#fff;text-align:center}
.card .photo{height:140px}
.card b{display:block;font-size:12px;color:#444;margin-top:10px}
.card small{display:block;font-size:11px;color:#666;line-height:16px}
.card .btn{margin-top:6px}
/* news */
.news-kicker{left:45px;top:1334px}
.news-title{left:48px;top:1360px;font-size:33px}
.news-card{top:1405px;width:280px}
.news-photo{height:190px}
.news-body{left:28px;top:112px;width:230px;height:140px;background:#fff;padding:14px 0 0 26px}
.news-body .date{font-size:13px;color:#555}
.news-body h4{font-family:"Open Sans",sans-serif;font-size:18px;color:var(--blue);font-weight:400;margin:6px 0 8px}
.news-body p{font-size:11.5px;line-height:18px;font-weight:300}
.news-btn{top:1644px}
.paper-kicker{left:695px;top:1334px}
.paper-title{left:694px;top:1358px;font-size:32px}
.paper-intro{left:695px;top:1404px;font-size:13.5px;font-weight:300;color:#444}
.paper-cover{left:694px;top:1440px;width:139px;height:196px;background:linear-gradient(#f7f6f1,#e0dccf);border:1px solid #ddd}
.paper-text{left:846px;top:1440px;width:310px;font-size:14px;font-weight:300;line-height:18.5px;color:#444}
.paper-text ol{margin-top:12px;padding-left:0;list-style-position:inside}
.paper-btn{left:1033px;top:1624px;padding:6px 18px}
/* contact */
.contact{top:1703px;left:0;width:1200px;height:450px;background:var(--grey)}
.contact-img{left:48px;top:1853px;width:326px;height:210px;background:linear-gradient(160deg,#b6d1ea,#d7d2c3 45%,#6f8c44 80%)}
.contact-brand{left:428px;top:1850px;width:130px;height:110px;display:flex;align-items:center;gap:10px}
.contact-brand .sq{width:26px;height:26px;background:var(--blue)}
.contact-brand b{font-family:"Comfortaa",sans-serif;color:var(--blue);font-size:16px}
.contact-list{left:430px;top:1978px;font-size:14px;line-height:27px;font-weight:300;color:#555}
.contact-list svg{fill:var(--blue)}
.form-label{left:731px;font-size:14px;font-weight:300;color:#555}
.form-label svg{fill:#777}
.field{left:731px;width:414px;height:42px;background:#fff}
.form-note{left:731px;top:2010px;width:250px;font-size:11.5px;line-height:14px;font-weight:300}
.form-btn{left:1035px;top:2013px;padding:6px 22px}
/* footer */
.footer-wave{left:0;top:2095px;width:1200px;height:415px}
.footer-brand{left:52px;top:2183px;display:flex;align-items:center;gap:10px}
.footer-brand .sq{width:24px;height:24px;background:var(--blue)}
.footer-brand b{font-family:"Comfortaa",sans-serif;color:var(--blue);font-size:16px}
.footer-list{left:52px;top:2292px;font-size:14px;line-height:26.5px;color:#fff;font-weight:300}
.footer-list svg{fill:#fff}
.footer h5{font-family:"Comfortaa",sans-serif;font-weight:600;color:#fff;font-size:22px;position:absolute;text-transform:uppercase}
.footer h5::after{content:"";display:block;width:90px;height:1px;background:#fff;margin-top:6px}
.footer-hours{left:498px;top:2243px;font-size:13px;line-height:22px;color:#fff;font-weight:300}
.footer-nav{left:954px;top:2243px;font-size:13px;line-height:19px;color:#fff;text-transform:uppercase;font-weight:300}
.footer-rule{left:44px;top:2416px;width:1097px;height:1px;background:#fff}
.copyright{top:2435px;font-size:15px;color:#fff;font-weight:300}
.footer-meta{top:2462px;font-size:11px;color:#fff}
.footer-meta span{margin:0 5px}
</style>
</head>
<body>

<header>
  <div class="abs topbar"></div>
  <div class="abs tagline">Gemeinschaft - ein Wort ein Programm!</div>
  <div class="abs havarie-top"><svg class="icon" style="fill:var(--red)" viewBox="0 0 16 16"><rect x="4" y="1" width="8" height="14" rx="1.5"/></svg>Havarienummer: 0176 / 555 019 0</div>
  <div class="abs meta-nav cond">SERVICE<span>|</span>MIETERZEITUNG<span>|</span>PARTNER<span>|</span>DOWNLOAD<span>|</span>IMPRESSUM<span>|</span>DATENSCHUTZERKLÄRUNG</div>

  <nav class="abs mainnav"></nav>
  <div class="abs brand-box"><span class="sq"></span><b>WBG Kelmsried</b></div>
  <div class="abs site-title deco" style="color:#fff">WOHNUNGSBAUGENOSSENSCHAFT KELMSRIED EG</div>
  <div class="abs nav-items cond"><span class="active">HOME</span>|<span>DIE GENOSSENSCHAFT</span>|<span>WOHNUNGSSUCHE</span>|<span>AKTUELLES</span>|<span>HAVARIEDIENST</span>|<span>KONTAKT</span></div>
</header>

<section class="hero abs" role="img" aria-label="Foto: lachende Frau mit Wohnungsschlüssel und lächelnder Mann"></section>
<h1 class="abs deco hero" style="background:none;height:auto;width:auto;left:603px;top:136px">Leben wo Sie sich<br>wohlfühlen</h1>
<p class="abs hero-copy">Ihr neues Zu Hause. Neue Wohnkonzepte<br>und ein angenehmes Wohnfeld. Bei uns<br>werden Sie glücklich!</p>
<a class="abs btn hero-btn">Zu den Wohnungsangeboten</a>

<section class="abs infobox" style="left:33px;background:var(--box1)">
  <h3><svg viewBox="0 0 20 20"><circle cx="10" cy="6" r="4.5"/><path d="M2 19c0-5 3.5-8 8-8s8 3 8 8z"/></svg>Kontakt</h3>
  <p><svg class="icon" viewBox="0 0 16 16"><path d="M8 1a5 5 0 0 0-5 5c0 4 5 9 5 9s5-5 5-9a5 5 0 0 0-5-5zm0 7a2 2 0 1 1 0-4 2 2 0 0 1 0 4z"/></svg>Am Lindenhang 13, 09417 Kelmsried<br>
  <svg class="icon" viewBox="0 0 16 16"><path d="M4 1h8v14H4zm2 2v9h4V3z"/></svg>03741 / 52 60<br>
  <svg class="icon" viewBox="0 0 16 16"><path d="M1 6c2-3 12-3 14 0l-2 2-2-1V5H5v2L3 8zM3 9h10v5H3z"/></svg>03741 / 52 619<br>
  <svg class="icon" viewBox="0 0 16 16"><path d="M1 3h14v10H1zm1 1v1l6 4 6-4V4z"/></svg>kontakt@wbg-kelmsried.example</p>
</section>
<section class="abs infobox hours" style="left:317px;background:var(--box2)">
  <h3><svg viewBox="0 0 20 20"><path d="M10 1a9 9 0 1 0 0 18 9 9 0 0 0 0-18zm0 2a7 7 0 1 1 0 14 7 7 0 0 1 0-14zM9 5v6l5 3 1-1.5-4-2.5V5z"/></svg>Öffnungszeiten</h3>
  <p><b>Mo.:</b> 09.00 - 12.00 Uhr &amp; 13.00 - 16.00 Uhr<br><b>Di.:</b>&nbsp;&nbsp;09.00 - 12.00 Uhr &amp; 13.00 - 18.00 Uhr<br><b>Mi.:</b>&nbsp;09.00 - 12.00 Uhr &amp; 13.00 - 16.00 Uhr<br><b>Do.:</b> 09.00 - 12.00 Uhr &amp; 13.00 - 16.00 Uhr<br><b>Fr.:</b>&nbsp;&nbsp;09.00 - 12.00 Uhr</p>
</section>
<section class="abs infobox" style="left:600px;background:var(--box3)">
  <h3><svg viewBox="0 0 20 20"><path d="M10 2 1 10h3v8h4v-5h4v5h4v-8h3z"/></svg>Freie Wohnungen</h3>
</section>
<div class="abs flat-card">
  <div class="abs flat-photo" role="img" aria-label="Foto: Wohnblock am Gartenweg"></div>
  <div class="abs txt">Kelmsried (09417)<br>Gartenweg 35<br>3. Obergeschoss<br>3-Raum<br>58,04 m²</div>
  <div class="abs dots">●●●</div>
</div>
<section class="abs infobox service" style="left:883px;background:var(--box4)">
  <h3><svg viewBox="0 0 20 20"><path d="M13 1a5 5 0 0 0-4.6 7L1.5 15a2 2 0 0 0 3 3l7-7A5 5 0 0 0 19 6l-3 3-3-1-1-3 3-3a5 5 0 0 0-2-1z"/></svg>Service / Havarie</h3>
  <p>Wir sind ständig bestrebt die Wohnqualität in unserer Genossenschaft zu steigern. Dazu gehört natürlich auch die Absicherung in Not-situationen. Unsere Havarienummer:</p>
  <div class="phone"><svg class="icon" style="width:17px;height:20px" viewBox="0 0 16 16"><path d="M4 1h8v14H4zm2 2v9h4V3z"/></svg>0176 / 555 0190</div>
</section>

<section class="welcome">
  <div class="abs welcome-img" role="img" aria-label="Foto: fröhliche Gruppe junger Menschen mit Daumen hoch"></div>
  <div class="abs kicker welcome-kicker">Ihre Wohnungsbaugenossenschaft Kelmsried eG</div>
  <h2 class="abs deco" style="left:504px;top:582px;font-size:29px">Herzlich Willkommen</h2>
  <p class="abs welcome-text">Informieren Sie sich über unsere Genossenschaft, das aktuelle Wohnungsangebot sowie über das umfangreiche Angebot an Dienstleistungen. Ob interessante Wohnungen, nach Ihren Wünschen gestaltet, ruhige Wohnlagen in 6 Gemeinden mit viel Grün, eine intakte Infrastruktur, vielseitigste Betreuungs-leistungen oder auch gemeinsame Freizeitaktivitäten und Feste - wir bieten für jede Generation genau das Richtige und stehen Ihnen als kompetenter Partner gern zur Verfügung.</p>
  <p class="abs signoff">Nehmen Sie mit uns Kontakt auf. Viel Spaß und eine gute Information wünscht Ihnen</p>
  <div class="abs signature" role="img" aria-label="Handschriftliche Unterschrift der Genossenschaft"></div>
</section>

<section class="abs market"></section>
<div class="abs center kicker" style="top:862px">Freie Wohnungen warten auf Sie</div>
<h2 class="abs center deco" style="top:882px;font-size:30px">Wohnungsmarkt</h2>
<p class="abs center" style="top:924px;font-size:12.5px;font-weight:300;color:#555">Informationen zu weiteren Wohnungsangeboten erhalten Sie persönlich oder auch telefonisch über unsere Geschäftsstelle.</p>
<ul class="abs market-list">
  <li class="active">Kelmsried (09417)</li>
  <li>Ahrnbach, OT Feldmark (09436)</li>
  <li>Holmsdorf (09432)</li>
  <li>Wiesenau (09441)</li>
  <li>Tarnitz (09449)</li>
  <li>Birkental (09428)</li>
</ul>
<h3 class="abs deco market-head">Wohnungen in Kelmsried</h3>
<article class="abs card" style="left:428px"><div class="photo" role="img" aria-label="Foto: mehrgeschossiger Wohnblock" style="background:linear-gradient(#9dc0e3,#e4d8b8 55%,#6b8e46)"></div><b>Kelmsried (09417)</b><small>3-Raum | 58,04 m²<br>Gartenweg 35, 3. Obergeschoss</small><a class="btn">Zu den Details</a></article>
<article class="abs card" style="left:682px"><div class="photo" role="img" aria-label="Foto: helles Wohnzimmer mit roten Vorhängen" style="background:linear-gradient(90deg,#e9e2d4,#d4552a 50%,#efe7da)"></div><b>Kelmsried (09417)</b><small>3-Raum | 58,04 m²<br>Gartenweg 35, 3. Obergeschoss</small><a class="btn">Zu den Details</a></article>
<article class="abs card" style="left:934px"><div class="photo" role="img" aria-label="Foto: Altbaufassade mit Bäumen" style="background:linear-gradient(90deg,#5d8a3c,#e8e4da 40%,#d8d2c4 70%,#6a8f40)"></div><b>Kelmsried (09417)</b><small>3-Raum | 58,04 m²<br>Gartenweg 35, 3. Obergeschoss</small><a class="btn">Zu den Details</a></article>

<section class="news">
  <div class="abs kicker news-kicker">Aktuelles für die Mieter</div>
  <h2 class="abs deco news-title">News</h2>
  <article class="abs news-card" style="left:44px">
    <div class="news-photo" role="img" aria-label="Foto: Versammlung in einem Saal" style="background:linear-gradient(#f3f1ec,#a3553a 45%,#6d5a48)"></div>
    <div class="abs news-body"><div class="date"><svg class="icon" viewBox="0 0 16 16"><path d="M2 3h12v12H2zm1 4v7h10V7zM4 1h2v3H4zm6 0h2v3h-2z"/></svg>26.07.2019</div><h4>Überschrift</h4><p>Lorem ipsum dolor sit amet,<br>sadipscing elitr, sed diam...</p></div>
  </article>
  <a class="abs btn news-btn" style="left:139px;padding:4px 16px">Mehr erfahren</a>
  <article class="abs news-card" style="left:343px;width:276px">
    <div class="news-photo" role="img" aria-label="Foto: Mieterfest im Freien" style="background:linear-gradient(#dfe9f3,#7e9a5a 45%,#5a6a48)"></div>
    <div class="abs news-body" style="left:24px"><div class="date"><svg class="icon" viewBox="0 0 16 16"><path d="M2 3h12v12H2zm1 4v7h10V7zM4 1h2v3H4zm6 0h2v3h-2z"/></svg>25.03.2018</div><h4>Überschrift</h4><p>Lorem ipsum dolor sit amet,<br>sadipscing elitr, sed diam...</p></div>
  </article>
  <a class="abs btn news-btn" style="left:430px;top:1642px;padding:4px 16px">Mehr erfahren</a>

  <div class="abs kicker paper-kicker">Schon entdeckt?</div>
  <h2 class="abs deco paper-title">Die Mieterzeitung</h2>
  <p class="abs paper-intro">Die 3.Ausgabe 2016 unserer Mieterzeitung steht zum Download bereit!</p>
  <div class="abs paper-cover" role="img" aria-label="Titelseite der Mieterzeitung Heft 03/2016"></div>
  <div class="abs paper-text">Die aktuelle Ausgabe unserer Mieterzeitung<br>Heft 03/2016
    <ol><li>24. Ordentliche Generalversammlung</li><li>Genossenschaftsfest am 20.August 2016<br>&nbsp;&nbsp;&nbsp;&nbsp;in Kelmsried</li><li>Kurz und bündig</li><li>Sommerhitze – Tipps für Senioren</li><li>14. Genossenschaftlicher Wandertag</li></ol>
  </div>
  <a class="abs btn paper-btn">Zum Archive</a>
</section>

<section class="abs contact"></section>
<div class="abs center kicker" style="top:1763px">Nehmen Sie Kontakt zu uns auf</div>
<h2 class="abs center deco" style="top:1780px;font-size:32px">Kontakt</h2>
<div class="abs contact-img" role="img" aria-label="Foto: Wohnhäuser mit Rasen und Bäumen"></div>
<div class="abs contact-brand"><span class="sq"></span><b>WBG Kelmsried</b></div>
<div class="abs contact-list">
  <div><svg class="icon" viewBox="0 0 16 16"><path d="M8 1a5 5 0 0 0-5 5c0 4 5 9 5 9s5-5 5-9a5 5 0 0 0-5-5zm0 7a2 2 0 1 1 0-4 2 2 0 0 1 0 4z"/></svg>Am Lindenhang 13, 09417 Kelmsried</div>
  <div><svg class="icon" viewBox="0 0 16 16"><path d="M4 1h8v14H4zm2 2v9h4V3z"/></svg>03741 / 52 60</div>
  <div><svg class="icon" viewBox="0 0 16 16"><path d="M1 6c2-3 12-3 14 0l-2 2-2-1V5H5v2L3 8zM3 9h10v5H3z"/></svg>03741 / 52619</div>
  <div><svg class="icon" viewBox="0 0 16 16"><path d="M1 3h14v10H1zm1 1v1l6 4 6-4V4z"/></svg>kontakt@wbg-kelmsried.example</div>
</div>
<div class="abs form-label" style="top:1850px"><svg class="icon" viewBox="0 0 20 20"><circle cx="10" cy="6" r="4.5"/><path d="M2 19c0-5 3.5-8 8-8s8 3 8 8z"/></svg>Ihr Vorname / Nachname*</div>
<div class="abs field" style="top:1873px"></div>
<div class="abs form-label" style="top:1928px"><svg class="icon" viewBox="0 0 20 20"><circle cx="10" cy="6" r="4.5"/><path d="M2 19c0-5 3.5-8 8-8s8 3 8 8z"/></svg>Ihre Nachricht*</div>
<div class="abs field" style="top:1952px"></div>
<p class="abs form-note">Die mit * gekennzeichneten Felder sind Pflichtfelder. Ihre Daten werden vertraulich behandelt.</p>
<a class="abs btn form-btn">Ab die Post</a>

<footer class="footer">
  <svg class="abs footer-wave" viewBox="0 0 1200 415" preserveAspectRatio="none"><path d="M0 0 Q600 110 1200 0 V415 H0z" fill="var(--lav)"/></svg>
  <div class="abs footer-brand"><span class="sq"></span><b>WBG Kelmsried</b></div>
  <div class="abs footer-list">
    <div><svg class="icon" viewBox="0 0 16 16"><path d="M8 1a5 5 0 0 0-5 5c0 4 5 9 5 9s5-5 5-9a5 5 0 0 0-5-5zm0 7a2 2 0 1 1 0-4 2 2 0 0 1 0 4z"/></svg>Am Lindenhang 13, 09417 Kelmsried</div>
    <div><svg class="icon" viewBox="0 0 16 16"><path d="M4 1h8v14H4zm2 2v9h4V3z"/></svg>03741 / 52 60</div>
    <div><svg class="icon" viewBox="0 0 16 16"><path d="M1 6c2-3 12-3 14 0l-2 2-2-1V5H5v2L3 8zM3 9h10v5H3z"/></svg>03741 / 52 619</div>
    <div><svg class="icon" viewBox="0 0 16 16"><path d="M1 3h14v10H1zm1 1v1l6 4 6-4V4z"/></svg>kontakt@wbg-kelmsried.example</div>
  </div>
  <h5 style="left:497px;top:2200px">Öffnungszeiten</h5>
  <div class="abs footer-hours" style="top:2240px"><b>Mo.:</b> 09.00 - 12.00 Uhr &amp; 13.00 - 16.00 Uhr<br><b>Di.:</b>&nbsp;&nbsp;09.00 - 12.00 Uhr &amp; 13.00 - 18.00 Uhr<br><b>Mi.:</b>&nbsp;09.00 - 12.00 Uhr &amp; 13.00 - 16.00 Uhr<br><b>Do.:</b> 09.00 - 12.00 Uhr &amp; 13.00 - 16.00 Uhr<br><b>Fr.:</b>&nbsp;&nbsp;09.00 - 12.00 Uhr</div>
  <h5 style="left:953px;top:2200px">Navigation</h5>
  <div class="abs footer-nav" style="top:2240px">Home<br>Die Genossenschaft<br>Wohnungssuche<br>Aktuelles<br>Havariedienst<br>Kontakt<br>Datenschutzerklärung</div>
  <div class="abs footer-rule"></div>
  <div class="abs center copyright">© Unternehmensname 2019. All rights reserved.</div>
  <div class="abs center footer-meta cond">SERVICE<span>|</span>MIETERZEITUNG<span>|</span>PARTNER<span>|</span>DOWNLOAD<span>|</span>IMPRESSUM<span>|</span>DATENSCHUTZERKLÄRUNG</div>
</footer>

</body>
</html>
```